Web Design Project

This as the foundation http://vorlintstudio.example/demo_viewer/index.php?theme=plaxiwp

Site needs to have a glossy black background with white text…..Extremely modern with a few flares of windows 8 style but nothing too off the wall, easily understood.

Here are some other reference sites and likes and dislikes that will help: (Probably overkill but we are looking for a cutting edge New York / LA Style )

http://www.bruvelgroupny.example

Like- The black background with white font is very eye catching and clean. Love the contrast. Black is a great background for photographs and videos

http://tomasgrell.example

Like- Clean homepage, black and white color scheme works well.

http://dwainkolbyphotography.example

Like- Nice Menu, nice B and W contrast

http://www.qvx.example

Like- Like the Menu. Clean and easy.

http://www.saffelmedia.example

Like- Contrast of white background with black font.

Like- Slide show of stills (but should be able to click images to go to video. We’d also like the name of the project)

Like- Drop down menu allows for customer to find service they need without going through all services.

Like- Tells you work that they do right next to the logo.

Dislike- Too much information on homepage. Too much scrolling.

http://www.corvanfilms.example

Like- High Res images on home page

Like - The About Me is on homepage and speaks to potential customer directly. “We create award-winning videos for companies like yours.”

Like- Blog is updated with new projects they do. And short, visual entries

Like- “Work” section stands out from website. The background fades to light grey and white when you click on “work” so that the portfolio stands out more. Makes color look more vivid

Like- Black and white color scheme with grey header

http://www.bureau478.example

Like- High Res images on home page pointing to projects

Like- Photograph as background, changes with different links. So work is always showcased and creates contrast. Information is laid over a barely translucent background, which is laid over the picture.

Like- They have a good Attitude about quality of their product

http://www.quillstone.example

Like- First thing you see when open page is a clear big statement about what they do, said in a catchy way. They have a Tagline.

http://tessurolab.example

Like- How work is categorized. Client list has links, which take you to their Client page with all their work grouped together. Nice flow and organization shows client relationships. And nice descriptions of what the job was and how it was executed… Way too wordy at times though

http://www.mirandelphotostudio.example

Like- The homepage is very clean and accessible. Love the color scheme and how Logo is centered between the links.
Updates

Of the four designs we have gotten EVERY SINGLE ONE has been a template STOLEN from another site. We are paying for ORIGINAL design. Not copies and templates. Please ONLY submit original designs

Industry/Entity Type

Foundation

```html
<!DOCTYPE html>
<html lang="en">
<head>
<meta charset="utf-8">
<title>Brassmoor Productions</title>
<link href="https://fonts.googleapis.com/css2?family=Oswald:wght@200;300;400&family=PT+Sans+Narrow:wght@400;700&family=Titillium+Web:ital,wght@1,900&display=swap" rel="stylesheet">
<style>
:root{
  --black:#000;
  --white:#fff;
  --ink:#111;
  --frame:#2b2b2b;
  --band-top:#5a5a5a;
  --band-mid:#1a1a1a;
  --text-soft:#d6d6d6;
  --field:#efefef;
  --field-line:#333;
  --muted:#9a9a9a;
}
*{box-sizing:border-box;margin:0;padding:0}
html,body{width:1021px;height:1200px;overflow:hidden}
body{
  position:relative;
  background:linear-gradient(var(--white) 0,var(--white) 596px,var(--black) 596px);
  font-family:"PT Sans Narrow",sans-serif;
  color:var(--white);
}
.hero-art{position:absolute;left:0;top:0}
.main-nav{position:absolute;top:8px;left:0;width:1021px;height:26px}
.main-nav a{
  position:absolute;top:0;color:var(--white);text-decoration:none;
  font-family:"Oswald",sans-serif;font-weight:300;font-size:17px;letter-spacing:-.3px;
  text-shadow:0 0 6px rgba(255,255,255,.35);
}
.brand-mark{
  position:absolute;left:400px;top:78px;width:220px;text-align:center;
  font-family:"Oswald",sans-serif;font-weight:200;font-size:19px;letter-spacing:2px;color:var(--white);
}
.thumb{
  position:absolute;width:139px;height:97px;border-radius:13px;
  border:6px solid var(--frame);overflow:hidden;
}
.thumb span{display:block;width:100%;height:100%;border-radius:7px}
.headline{position:absolute;left:336px;top:188px;width:358px;text-align:center;color:var(--ink)}
.headline .lead{font-family:"Titillium Web",sans-serif;font-style:italic;font-weight:900;font-size:31px;line-height:36px;letter-spacing:-.5px}
.headline .sub{font-family:"Oswald",sans-serif;font-weight:200;font-size:36px;line-height:38px;letter-spacing:-1px}
.reel{
  position:absolute;left:336px;top:271px;width:357px;height:189px;border-radius:20px;
  border:6px solid var(--ink);overflow:hidden;
}
.reel .still{width:100%;height:100%;background:linear-gradient(100deg,#bfe3f0 0%,#6fb9d4 38%,#d8eef5 70%,#9fd2e3 100%)}
.reel svg{position:absolute;left:299px;top:136px}
.studio-card{position:absolute;left:300px;top:508px;width:400px;text-align:center}
.studio-card h2{font-size:15px;font-weight:700;text-shadow:0 1px 2px #000}
.studio-card p{font-size:11.5px;color:var(--text-soft);margin-top:1px}
.col-title{font-family:"Oswald",sans-serif;font-weight:300;font-size:28px;line-height:34px;position:absolute;letter-spacing:-.5px}
.col-text{position:absolute;font-size:11.7px;line-height:14.3px;color:var(--text-soft)}
.more{position:absolute;font-size:12.5px;color:var(--white)}
.services-title{position:absolute;left:113px;top:796px;font-family:"Oswald",sans-serif;font-weight:300;font-size:16px;line-height:19px;width:400px;letter-spacing:-.3px}
.service-list{position:absolute;top:851px;list-style:none;font-size:12.6px;line-height:16.4px;color:var(--text-soft)}
.quote-label{position:absolute;right:109px;top:827px;font-size:12px}
.quote-form{position:absolute;left:646px;top:848px;width:273px;height:218px;background:var(--white);border-radius:9px;color:var(--ink)}
.quote-form label{position:absolute;left:15px;font-size:11px}
.quote-form .field{position:absolute;left:68px;width:187px;height:19px;background:var(--field);border:1px solid var(--field-line)}
.quote-form .field.tall{height:70px}
.quote-form button{
  position:absolute;left:69px;top:187px;width:63px;height:24px;background:var(--ink);color:var(--white);
  border:0;border-radius:2px;font-family:"PT Sans Narrow",sans-serif;font-size:11px;
}
.copyright{position:absolute;left:115px;top:1171px;font-size:11.5px;color:var(--muted)}
.contact-strip{position:absolute;left:605px;top:1158px;width:208px;height:36px;background:#0d0d0d;font-size:8px;color:#aaa;padding:13px 7px;white-space:nowrap;font-family:"PT Sans Narrow",sans-serif}
.share{position:absolute;left:818px;top:1167px;font-family:"Oswald",sans-serif;font-weight:300;font-size:13px;letter-spacing:-.5px}
.share-dot{position:absolute;top:1163px;width:24px;height:24px;border-radius:50%;background:#8a8a8a}
</style>
</head>
<body>

<svg class="hero-art" width="1021" height="600" viewBox="0 0 1021 600" aria-hidden="true">
  <defs>
    <linearGradient id="topBand" x1="0" y1="0" x2="0" y2="1">
      <stop offset="0" stop-color="#0a0a0a"/>
      <stop offset=".45" stop-color="#3c3c3c"/>
      <stop offset="1" stop-color="#0e0e0e"/>
    </linearGradient>
    <linearGradient id="baseBand" x1="0" y1="0" x2="0" y2="1">
      <stop offset="0" stop-color="#6a6a6a"/>
      <stop offset=".5" stop-color="#2a2a2a"/>
      <stop offset="1" stop-color="#000"/>
    </linearGradient>
  </defs>
  <path d="M93,0 H928 V98 C870,58 760,52 660,98 C590,132 560,157 510,157 C460,157 430,132 360,98 C260,52 150,58 93,98 Z" fill="url(#topBand)"/>
  <path d="M93,98 C150,58 260,52 360,98 C430,132 460,157 510,157 C560,157 590,132 660,98 C760,52 870,58 928,98" fill="none" stroke="#000" stroke-width="4"/>
  <path d="M93,556 C250,538 360,484 510,484 C660,484 770,538 928,556 V600 H93 Z" fill="#000"/>
  <path d="M98,566 C250,550 360,498 510,498 C660,498 770,550 933,566 V600 H98 Z" fill="url(#baseBand)" opacity=".85"/>
  <path d="M93,578 C300,562 720,562 933,578 V600 H93 Z" fill="#000" opacity=".55"/>
</svg>

<nav class="main-nav">
  <a style="left:139px">HOME</a>
  <a style="left:203px">ABOUT US</a>
  <a style="left:292px">REELS</a>
  <a style="left:357px">VIDEO GALLERY</a>
  <a style="left:474px">PHOTO GALLERY</a>
  <a style="left:596px">VIDEO BLOG</a>
  <a style="left:694px">CLIENTS</a>
  <a style="left:771px">FAQ</a>
  <a style="left:824px">CONACT US</a>
</nav>

<div class="brand-mark">Brassmoor Productions</div>

<div class="thumb" style="left:123px;top:106px"><span role="img" aria-label="Band portrait in a dim room" style="background:linear-gradient(135deg,#3a2a24,#8a6a55,#2a201c)"></span></div>
<div class="thumb" style="left:123px;top:251px"><span role="img" aria-label="Crowd at a lively party" style="background:linear-gradient(135deg,#6a3a4a,#c28a52,#3a4a7a)"></span></div>
<div class="thumb" style="left:123px;top:403px"><span role="img" aria-label="Yellow taxi on a city street" style="background:linear-gradient(160deg,#6a7a8a,#b9a860,#8a8f96)"></span></div>
<div class="thumb" style="left:762px;top:106px"><span role="img" aria-label="Wedding couple embracing" style="background:linear-gradient(135deg,#2a2220,#d8cfc6,#5a3a2a)"></span></div>
<div class="thumb" style="left:762px;top:251px"><span role="img" aria-label="Dancers in costume on a white stage" style="background:linear-gradient(135deg,#e6e2d6,#b7c48a,#d8d4c8)"></span></div>
<div class="thumb" style="left:762px;top:403px"><span role="img" aria-label="Phone with colourful tiles" style="background:linear-gradient(135deg,#111,#2a6aa0,#c03a8a)"></span></div>

<div class="headline">
  <div class="lead">FULL SERVICE HD</div>
  <div class="sub">VIDEO PRODUCTION</div>
</div>

<div class="reel">
  <div class="still" role="img" aria-label="Featured reel still: a hand touching pale blue water"></div>
  <svg width="36" height="36" viewBox="0 0 36 36" aria-hidden="true">
    <circle cx="18" cy="18" r="16" fill="none" stroke="#fff" stroke-width="2"/>
    <path d="M10,18 H24 M19,12 L25,18 L19,24" fill="none" stroke="#fff" stroke-width="2.5"/>
  </svg>
</div>

<div class="studio-card">
  <h2>Brassmoor Productions</h2>
  <p>48 W.31st Street, Suite 210, New York, NY 10001 212-555-0147</p>
</div>

<h1 class="col-title" style="left:118px;top:610px">ABOUT US</h1>
<p class="col-text" style="left:118px;top:655px;width:360px">&nbsp;Our New York City-based video production company offers a full &nbsp;top full service video studio and work in a wide range of media and styles. For over 30 years we have specialized in all aspects of video production from commercials and training video to legal video and video for non-profit organizations.</p>
<a class="more" style="left:119px;top:720px">MORE</a>

<h2 class="col-title" style="left:644px;top:611px">Over 30 Years Of Experience</h2>
<p class="col-text" style="left:644px;top:656px;width:268px">&nbsp;Our New York City-based video production company offers a full range of video production services, from storyboarding and scriptwriting to videotaping, post production editing and graphic design. We are a one-stop full service video studio and work in a wide range of media and styles. For over 30 years we have specialized in all aspects of video production from commercials and training video to legal video and video for non-profit organizations.</p>
<a class="more" style="left:645px;top:777px">MORE</a>

<h3 class="services-title">High definition video, location, and studio shoots, post production with award winning editors.</h3>
<ul class="service-list" style="left:115px">
  <li>Crowd-sourcing and Promotional</li>
  <li>Commercials</li>
  <li>Promotional Videos</li>
  <li>Corporate Videos</li>
  <li>Documentaries</li>
</ul>
<ul class="service-list" style="left:289px">
  <li>Event Video and Photography</li>
  <li>Oral Histories</li>
  <li>Training Videos</li>
  <li>Webcasting</li>
  <li>Multilingual Video Translation</li>
  <li>Music Videos</li>
</ul>

<div class="quote-label">Contact Us For A Free Quote</div>
<form class="quote-form">
  <label style="top:24px">name :</label><span class="field" style="top:17px"></span>
  <label style="top:54px">email :</label><span class="field" style="top:47px"></span>
  <label style="top:85px">website :</label><span class="field" style="top:76px"></span>
  <label style="top:115px">message :</label><span class="field tall" style="top:107px"></span>
  <button type="button">submit</button>
</form>

<div class="copyright">©2013 Brassmoor Productions All Rights Reserved.</div>
<div class="contact-strip">646.555.0192 &nbsp;|&nbsp; dwain@dwainkolbyphotography.example</div>
<div class="share">SHARE</div>
<span class="share-dot" style="left:853px" aria-label="Share link"></span>
<span class="share-dot" style="left:882px" aria-label="Share link"></span>

</body>
</html>
```